Dental Office Business Card

We need a business card for our pediatric dentistry office.
On one side the design needs to contain the following:
our logo (attached)
Vento Pediatric Grins
Soraya Kadbelani, DDS
Board Certified Pediatric Dentist
Tel: (555) 318-2747)
Fax: (555) 264-8031
Email: info@ventopediatricgrins.example
Web: www.ventopediatricgrins.example
Address: 41 Brindle Ave, Suite 208, Marrowby, NH 03999

On the other side of the card, the design needs to have an appointment reminder (date and time as well as day of the week) similar to the design attached (no need for appointment reason “For”)

```html
<!DOCTYPE html>
<html lang="en">
<head>
<meta charset="utf-8">
<title>Vento Pediatric Grins – Business Card</title>
<link href="https://fonts.googleapis.com/css2?family=Arimo:wght@400;600;700&family=Montserrat:wght@500&family=Cinzel:wght@400&display=swap" rel="stylesheet">
<style>
  :root {
    --stage-centre: #2a2a2a;
    --stage-edge: #050505;
    --card: #ffffff;
    --mint: #a9d6ab;
    --mint-rule: #86b889;
    --leaf: #7dbc80;
    --sage: #6e9a72;
    --ink: #1b1b1b;
    --ink-soft: #333333;
  }
  * { margin: 0; padding: 0; box-sizing: border-box; }
  html, body { width: 1200px; height: 1000px; overflow: hidden; }
  body {
    position: relative;
    background: radial-gradient(ellipse at center, var(--stage-centre) 0%, var(--stage-edge) 75%);
    font-family: "Arimo", Arial, sans-serif;
    color: var(--ink);
  }
  .card {
    position: absolute;
    left: 203px;
    width: 794px;
    height: 453px;
    background: var(--card);
    border-radius: 18px;
    overflow: hidden;
  }
  .card--front { top: 36px; }
  .card--back { top: 511px; }

  /* Front */
  .brand-mark {
    position: absolute; left: 34px; top: 62px;
    display: flex; align-items: center; gap: 12px;
    font-size: 30px; font-weight: 700; color: var(--ink);
  }
  .brand-mark__dot { width: 26px; height: 26px; border-radius: 50%; background: var(--mint); }
  .brand-emblem {
    position: absolute; left: 500px; top: 40px;
    width: 220px; height: 220px; border-radius: 50%;
    background: var(--mint);
  }
  .practice-name {
    position: absolute; left: 34px; top: 174px;
    font-size: 31px; font-weight: 700; color: var(--ink);
  }
  .practice-name__accent { color: var(--leaf); }
  .dentist {
    position: absolute; left: 34px; top: 214px;
    font-size: 20px; font-weight: 600; line-height: 29px; color: var(--ink);
  }
  .contact-band {
    position: absolute; left: 0; top: 289px; width: 100%; height: 164px;
    background: var(--mint);
  }
  .contact {
    position: absolute; display: flex; align-items: center; gap: 12px;
    font-size: 20px; color: var(--ink);
  }
  .contact__icon {
    width: 24px; height: 24px; background: #fff; border-radius: 4px;
    display: flex; align-items: center; justify-content: center;
  }
  .contact--tel { left: 36px; top: 21px; }
  .contact--fax { left: 36px; top: 56px; }
  .contact--mail { left: 422px; top: 21px; }
  .contact--web { left: 422px; top: 56px; }
  .contact-rule {
    position: absolute; left: 34px; right: 34px; top: 102px;
    border-top: 1px solid var(--mint-rule);
  }
  .address {
    position: absolute; left: 0; right: 0; top: 115px;
    display: flex; justify-content: center; align-items: center; gap: 8px;
    font-family: "Montserrat", Arial, sans-serif; font-weight: 500;
    font-size: 17px; text-transform: uppercase; color: var(--ink);
  }

  /* Back */
  .reminder-title {
    position: absolute; left: 0; right: 0; top: 24px; text-align: center;
    font-family: "Cinzel", Georgia, serif; font-weight: 400;
    font-size: 56px; line-height: 62px; letter-spacing: 0;
    color: var(--sage);
  }
  .reminder-sub {
    position: absolute; left: 0; right: 0; top: 82px;
    display: flex; justify-content: center; align-items: center; gap: 6px;
    font-family: "Cinzel", Georgia, serif; font-size: 28px;
    letter-spacing: 6px; color: var(--ink-soft);
  }
  .reminder-sub__dot { width: 22px; height: 22px; border-radius: 50%; background: var(--mint); }
  .field { position: absolute; left: 35px; font-size: 28px; color: var(--ink); }
  .field__line { position: absolute; border-top: 2px solid var(--ink); }
  .field--for { top: 166px; }
  .field--date { top: 228px; }
  .field--time { top: 378px; }
  .line--for { left: 138px; width: 621px; top: 190px; }
  .line--date { left: 138px; width: 621px; top: 252px; }
  .line--time { left: 138px; width: 282px; top: 402px; }
  .meridiem { position: absolute; left: 440px; top: 386px; font-size: 20px; color: var(--ink-soft); }
  .weekdays { position: absolute; left: 35px; top: 307px; width: 724px; height: 32px; }
  .weekday {
    position: absolute; top: 0; display: flex; align-items: center; gap: 10px;
    font-size: 24px; color: var(--ink-soft);
  }
  .weekday__box { width: 30px; height: 30px; border: 2px solid var(--ink); border-radius: 4px; }
</style>
</head>
<body>

<section class="card card--front">
  <div class="brand-mark"><span class="brand-mark__dot"></span>Vento Pediatric Grins</div>
  <div class="brand-emblem" role="img" aria-label="Practice emblem area"></div>

  <h1 class="practice-name"><span class="practice-name__accent">Vento</span> Pediatric Grins</h1>
  <p class="dentist">Soraya Kadbelani, DDS<br>Board Certified Pediatric Dentist</p>

  <div class="contact-band">
    <div class="contact contact--tel">
      <span class="contact__icon"><svg width="12" height="16" viewBox="0 0 12 16"><rect x="1" y="0.5" width="10" height="15" rx="2" fill="#1b1b1b"/><rect x="3" y="2.5" width="6" height="9" fill="#fff"/></svg></span>
      (555) 318-2747)
    </div>
    <div class="contact contact--fax">
      <span class="contact__icon"><svg width="16" height="15" viewBox="0 0 16 15"><rect x="4" y="0" width="8" height="4" fill="#1b1b1b"/><rect x="0" y="4" width="16" height="7" rx="1.5" fill="#1b1b1b"/><rect x="4" y="9" width="8" height="6" fill="#1b1b1b" stroke="#fff" stroke-width="1"/></svg></span>
      (555) 264-8031
    </div>
    <div class="contact contact--mail">
      <span class="contact__icon"><svg width="15" height="15" viewBox="0 0 15 15"><path d="M0 7 L15 0 L10 15 L7 9 Z" fill="#1b1b1b"/></svg></span>
      info@ventopediatricgrins.example
    </div>
    <div class="contact contact--web">
      <span class="contact__icon"><svg width="16" height="16" viewBox="0 0 16 16" fill="none" stroke="#1b1b1b" stroke-width="1.6"><circle cx="8" cy="8" r="7"/><ellipse cx="8" cy="8" rx="3" ry="7"/><path d="M1 8h14"/></svg></span>
      www.ventopediatricgrins.example
    </div>
    <div class="contact-rule"></div>
    <div class="address">
      <svg width="16" height="21" viewBox="0 0 16 21"><path d="M8 0a8 8 0 0 1 8 8c0 6-8 13-8 13S0 14 0 8a8 8 0 0 1 8-8z" fill="#1b1b1b"/><circle cx="8" cy="8" r="3" fill="#a9d6ab"/></svg>
      41 Brindle Ave, Suite 208, Marrowby, NH 03999
    </div>
  </div>
</section>

<section class="card card--back">
  <h2 class="reminder-title">APPOINTMENT</h2>
  <div class="reminder-sub"><span class="reminder-sub__dot"></span>REMINDER<span class="reminder-sub__dot"></span></div>

  <div class="field field--for">FOR&nbsp; :</div>
  <div class="field__line line--for"></div>
  <div class="field field--date">DATE :</div>
  <div class="field__line line--date"></div>

  <div class="weekdays">
    <span class="weekday" style="left:0"><span class="weekday__box"></span>Mon</span>
    <span class="weekday" style="left:116px"><span class="weekday__box"></span>Tue</span>
    <span class="weekday" style="left:221px"><span class="weekday__box"></span>Wed</span>
    <span class="weekday" style="left:338px"><span class="weekday__box"></span>Thu</span>
    <span class="weekday" style="left:445px"><span class="weekday__box"></span>Fri</span>
    <span class="weekday" style="left:540px"><span class="weekday__box"></span>Sat</span>
    <span class="weekday" style="left:642px"><span class="weekday__box"></span>Sun</span>
  </div>

  <div class="field field--time">TIME&nbsp; :</div>
  <div class="field__line line--time"></div>
  <div class="meridiem">a.m.&nbsp; p.m.</div>
</section>

</body>
</html>
```